RWM Electrical Business Card Design

Have a logo to use, just looking for design around this, would like green theme, would like symbols in place of phone, fax, email etc.

Business

RWM Electrical, Marcus Thorley, marcus@rwmelectrical.example.au, www.rwmelectrical.example.au, mobile 0491 568 342, phone (07) 3915 4280, fax (07) 3915 4280, facebook and linkedin
addresses

```html
<!DOCTYPE html>
<html lang="en">
<head>
<meta charset="utf-8">
<title>RWM Electrical Business Card</title>
<link rel="stylesheet" href="https://fonts.googleapis.com/css2?family=Questrial&family=Oswald:wght@500&display=swap">
<style>
  :root {
    --backdrop: #dcdde0;
    --card: #ffffff;
    --ink: #2b2b2b;
    --muted: #6a6a6a;
    --rule: #b9b9b9;
    --green: #3db54a;
  }
  * { box-sizing: border-box; margin: 0; padding: 0; }
  html, body { width: 1200px; height: 988px; overflow: hidden; }
  body {
    background: var(--backdrop);
    font-family: "Questrial", "Century Gothic", sans-serif;
    color: var(--ink);
    position: relative;
  }
  .card {
    position: absolute;
    left: 250px;
    width: 700px;
    height: 400px;
    background: var(--card);
    box-shadow: 0 6px 18px rgba(0,0,0,0.18);
  }
  .card--front { top: 70px; }
  .card--back { top: 518px; }

  .brand { display: flex; align-items: center; gap: 14px; }
  .brand__dot {
    width: 52px; height: 52px; border-radius: 50%;
    background: var(--green);
    flex: none;
  }
  .brand__name {
    font-size: 56px; font-weight: 400; color: var(--ink);
    letter-spacing: 0.5px; line-height: 1;
  }
  .card--front .brand { position: absolute; left: 150px; top: 168px; }

  .card--back .brand { position: absolute; left: 52px; top: 48px; }
  .card--back .brand__dot { width: 40px; height: 40px; }
  .card--back .brand__name { font-size: 42px; }
  .top-rule {
    position: absolute; left: 420px; right: 24px; top: 84px;
    height: 1px; background: var(--rule);
  }

  .person { position: absolute; left: 52px; top: 130px; }
  .person__name {
    font-family: "Oswald", "Arial Narrow", sans-serif;
    font-weight: 500; font-size: 24px; color: var(--green);
    letter-spacing: 1px; text-transform: uppercase; line-height: 1.1;
  }
  .person__title {
    font-size: 11px; color: var(--muted); letter-spacing: 1.5px;
    text-transform: uppercase; margin-top: 2px;
  }

  .contact-list { position: absolute; list-style: none; }
  .contact-list--left { left: 52px; top: 190px; width: 230px; }
  .contact-list--right { left: 330px; top: 110px; width: 280px; }
  .contact {
    display: flex; align-items: center; gap: 12px;
    height: 44px; border-bottom: 1px solid var(--rule);
    font-size: 13px; color: var(--ink); letter-spacing: 0.3px;
  }
  .contact__icon {
    width: 26px; height: 26px; background: var(--green);
    border-radius: 4px; flex: none;
    display: flex; align-items: center; justify-content: center;
  }
  .contact__icon svg { width: 16px; height: 16px; fill: none; stroke: #fff; stroke-width: 1.8; stroke-linecap: round; stroke-linejoin: round; }
</style>
</head>
<body>
  <section class="card card--front">
    <div class="brand">
      <span class="brand__dot"></span>
      <span class="brand__name">RWM Electrical</span>
    </div>
  </section>

  <section class="card card--back">
    <div class="brand">
      <span class="brand__dot"></span>
      <span class="brand__name">RWM Electrical</span>
    </div>
    <div class="top-rule"></div>

    <div class="person">
      <div class="person__name">Marcus Thorley</div>
      <div class="person__title">Financial Advisor</div>
    </div>

    <ul class="contact-list contact-list--left">
      <li class="contact">
        <span class="contact__icon"><svg viewBox="0 0 24 24"><rect x="7" y="3" width="10" height="18" rx="2"/><line x1="11" y1="18" x2="13" y2="18"/></svg></span>
        <span>0491 568 342</span>
      </li>
      <li class="contact">
        <span class="contact__icon"><svg viewBox="0 0 24 24"><path d="M5 4h4l2 5-2.5 1.5a11 11 0 0 0 5 5L15 13l5 2v4a2 2 0 0 1-2 2A16 16 0 0 1 3 6a2 2 0 0 1 2-2z"/></svg></span>
        <span>(07) 3915 4280</span>
      </li>
      <li class="contact">
        <span class="contact__icon"><svg viewBox="0 0 24 24"><path d="M12 21s-6-6.2-6-11a6 6 0 0 1 12 0c0 4.8-6 11-6 11z"/><circle cx="12" cy="10" r="2.2"/></svg></span>
        <span>12 Example Road, Brisbane QLD</span>
      </li>
    </ul>

    <ul class="contact-list contact-list--right">
      <li class="contact">
        <span class="contact__icon"><svg viewBox="0 0 24 24"><rect x="3" y="6" width="18" height="12" rx="1.5"/><path d="M3 7l9 6 9-6"/></svg></span>
        <span>marcus@rwmelectrical.example.au</span>
      </li>
      <li class="contact">
        <span class="contact__icon"><svg viewBox="0 0 24 24"><circle cx="12" cy="12" r="9"/><path d="M3 12h18M12 3c3 3 3 15 0 18M12 3c-3 3-3 15 0 18"/></svg></span>
        <span>www.rwmelectrical.example.au</span>
      </li>
    </ul>
  </section>
</body>
</html>
```